The Shelf Sage needs a pricing flyer

Single page flyer for the Shelf Sage.
The Shelf Sage is a lead generation service exclusively for the custom closet industry.
You design quality closets we provide quality leads!
Value Points:
Leads for closet companies are exclusive with a first right of refusal. Meaning, if the closet company cannot handle all of the leads we can provide, we will sell the excess to other closet companies. We will never sell the same lead to two different closet companies.
Benefits:
Flat rate and easy to budget
Cancel at anytime
Choose from 3 types of leads
Lower cost compared to overall cost per lead from other sources
More leads allows hiring more designers
More leads grow the companies revenue
Less time managing other advertising models
3 service options.
$250 each
- We send you the lead
- You and your team set the appointment
- Setting the appointment is up to you
2. $275 each
- We send you the lead
- We guarantee the appointment
- Return unset appointments for a replacement
3. $375 each
- We are your call center
- We generate the lead
- We set the appointment
Contact:
The Shelf Sage
704-555-0183
leads@TheShelfSage.example

```html
<!DOCTYPE html>
<html lang="en">
<head>
<meta charset="utf-8">
<title>The Shelf Sage – Pricing Flyer</title>
<link href="https://fonts.googleapis.com/css2?family=Vollkorn:wght@500;600;700&family=Poppins:wght@400;500;600&family=Great+Vibes&display=swap" rel="stylesheet">
<style>
:root{
  --brown:#a45f28;
  --brown-dark:#8a4d1f;
  --tan:#d9c2ab;
  --slate:#57565a;
  --ink:#2e2e30;
  --paper:#ffffff;
  --stage:#eceef0;
  --serif:'Vollkorn', Georgia, serif;
  --sans:'Poppins', Arial, sans-serif;
  --script:'Great Vibes', cursive;
}
*{margin:0;padding:0;box-sizing:border-box}
html,body{width:1200px;height:2282px;overflow:hidden;background:var(--stage)}
.flyer{position:absolute;left:0;top:364px;width:944px;height:1222px;background:var(--paper);
  transform:scale(1.2712);transform-origin:0 0;overflow:hidden;font-family:var(--sans);color:var(--ink)}
.abs{position:absolute}

.hero-photo{left:0;top:0;width:944px;height:545px;
  background:linear-gradient(100deg,#d8d4cf 0%,#ebe8e4 35%,#e4dfd8 60%,#c9bfb3 80%,#a99a8a 100%)}
.hero-photo-left{left:0;top:545px;width:570px;height:90px;background:#cfc9c2}
.title-panel{left:28px;top:0;width:474px;height:460px;background:rgba(255,255,255,.72);text-align:center}
.brand-top{top:125px;width:100%;font-family:var(--serif);font-weight:500;font-size:30px;color:var(--slate)}
.headline-1{top:178px;width:100%;font-family:var(--serif);font-weight:700;font-size:50px;color:var(--brown);line-height:1}
.headline-2{top:232px;width:100%;font-family:var(--serif);font-weight:700;font-size:39px;color:var(--brown);line-height:1}
.headline-3{top:278px;left:-14px;width:100%;font-family:var(--script);font-size:44px;color:var(--slate);line-height:1}
.rule{left:216px;top:345px;width:42px;height:5px;background:var(--brown)}
.tagline{top:362px;width:100%;font-family:var(--serif);font-weight:600;font-size:26px;line-height:33px;color:var(--slate)}

.refusal-band{left:0;top:512px;width:572px;height:120px;background:var(--slate);padding:14px 0 0 46px;color:#fff}
.refusal-band h2{font-family:var(--serif);font-style:italic;font-weight:500;font-size:16.5px;color:#e39a57;margin-bottom:3px}
.refusal-band p{font-size:14.5px;line-height:18.5px;width:515px}

.inset-frame{left:570px;top:375px;width:336px;height:291px;background:#c9956a;border-radius:6px;padding:9px}
.inset-photo{width:100%;height:100%;border:2px solid #fff;
  background:radial-gradient(ellipse at 50% 85%,#efe6dc 0%,#b79a80 30%,#5a3a28 60%,#2c1c14 100%)}

.benefits-title{left:46px;top:647px;font-family:var(--serif);font-weight:600;font-size:31px;color:var(--brown)}
.benefits-frame{left:150px;top:670px;width:241px;height:436px;border-top:1px solid var(--brown);border-right:1px solid var(--brown);border-bottom:1px solid var(--brown);border-radius:0 8px 8px 0}
.benefits-frame::before{content:"";position:absolute;left:-155px;bottom:-1px;width:155px;border-bottom:1px solid var(--brown)}
.benefit-list{left:50px;top:690px;width:325px;list-style:none}
.benefit{height:59px;display:flex;align-items:center;gap:16px;position:relative}
.benefit::after{content:"";position:absolute;left:10px;right:0;bottom:2px;height:3px;background:linear-gradient(90deg,#d3d3d3,#f2f2f2 90%,transparent)}
.benefit-icon{flex:none;width:46px;height:44px;background:var(--brown);border-radius:4px 12px 4px 12px;display:flex;align-items:center;justify-content:center}
.benefit-text{font-size:15.5px;line-height:18px;color:#222}

.services-label{left:352px;top:842px;width:180px;transform:rotate(-90deg);text-align:center;
  font-family:var(--serif);font-weight:600;font-size:29px;color:var(--brown);letter-spacing:.5px;line-height:1}
.services-line{left:430px;width:1px;background:var(--brown)}
.price{width:108px;height:108px;border-radius:50%;border:6px solid var(--tan);text-align:center;color:var(--brown)}
.price-amount{display:block;font-family:var(--serif);font-weight:600;font-size:38px;line-height:1;margin-top:20px}
.price-amount sup{font-size:17px;vertical-align:16px}
.price-each{display:block;font-size:17px;letter-spacing:3px;color:var(--ink);line-height:1;margin-top:0}
.plan{left:598px;width:300px;list-style:none}
.plan li{position:relative;padding-left:22px;font-size:15px;line-height:17px;margin-bottom:6px}
.plan li svg{position:absolute;left:0;top:2px}
.divider{left:598px;width:300px;border-top:1px dashed #9a9a9a}

.brand-footer{left:46px;top:1118px;font-family:var(--serif);font-weight:600;font-size:42px;color:var(--slate)}
.contact{left:448px;top:1111px;display:flex;gap:14px;font-size:17px;color:#222;align-items:center}
.contact span{display:flex;align-items:center;gap:7px}
.web-bar{left:443px;top:1140px;width:501px;height:35px;background:var(--brown);color:#fff;display:flex;align-items:center;gap:8px;padding-left:12px;font-size:17.5px;letter-spacing:3.2px}
.web-bar b{font-weight:600}
</style>
</head>
<body>
<main class="flyer">
  <div class="abs hero-photo" role="img" aria-label="Bright white custom walk-in closet with shelving full of shoes"></div>
  <div class="abs hero-photo-left" role="img" aria-label="Closet interior continued behind the value band"></div>

  <header class="abs title-panel">
    <div class="abs brand-top">The Shelf Sage</div>
    <h1 class="abs headline-1">A lead Generation</h1>
    <div class="abs headline-2">Service Exclusively for</div>
    <div class="abs headline-3">The custom Closet Industry</div>
    <div class="abs rule"></div>
    <p class="abs tagline">You design quality closets<br>we provide quality leads!</p>
  </header>

  <section class="abs refusal-band">
    <h2>Leads for closet companies are exclusive with a first right of refusal.</h2>
    <p>Meaning, if the closet company cannot handle all of the leads we can provide, we will sell the excess to other closet companies. We will never sell the same lead to two different closet companies.</p>
  </section>

  <div class="abs inset-frame"><div class="inset-photo" role="img" aria-label="Woman standing in a dark wood walk-in closet with central island"></div></div>

  <h2 class="abs benefits-title">Benefits</h2>
  <div class="abs benefits-frame"></div>
  <ul class="abs benefit-list">
    <li class="benefit"><span class="benefit-icon"><svg width="24" height="24" viewBox="0 0 24 24" fill="none" stroke="#fff" stroke-width="1.5"><path d="M5 19L19 5"/><circle cx="7" cy="7" r="2.5"/><circle cx="17" cy="17" r="2.5"/></svg></span><span class="benefit-text">Flat rate and easy to budget</span></li>
    <li class="benefit"><span class="benefit-icon"><svg width="24" height="24" viewBox="0 0 24 24" fill="none" stroke="#fff" stroke-width="1.5"><circle cx="12" cy="12" r="8"/><path d="M6 18L18 6"/></svg></span><span class="benefit-text">Cancel at anytime</span></li>
    <li class="benefit"><span class="benefit-icon"><svg width="24" height="24" viewBox="0 0 24 24" fill="none" stroke="#fff" stroke-width="1.5"><rect x="4" y="4" width="7" height="7"/><rect x="13" y="4" width="7" height="7"/><rect x="4" y="13" width="7" height="7"/></svg></span><span class="benefit-text">Choose from 3 types of leads</span></li>
    <li class="benefit"><span class="benefit-icon"><svg width="24" height="24" viewBox="0 0 24 24" fill="none" stroke="#fff" stroke-width="1.5"><circle cx="12" cy="12" r="8"/><path d="M12 7v10M9.5 9.5h4a1.5 1.5 0 010 3h-3a1.5 1.5 0 000 3h4"/></svg></span><span class="benefit-text">Lower cost compared to overall cost per lead from other sources</span></li>
    <li class="benefit"><span class="benefit-icon"><svg width="24" height="24" viewBox="0 0 24 24" fill="none" stroke="#fff" stroke-width="1.5"><circle cx="8" cy="8" r="2.5"/><circle cx="16" cy="8" r="2.5"/><path d="M4 18c0-3 2-5 4-5s4 2 4 5M12 18c0-3 2-5 4-5s4 2 4 5"/></svg></span><span class="benefit-text">More leads allows hiring more designers</span></li>
    <li class="benefit"><span class="benefit-icon"><svg width="24" height="24" viewBox="0 0 24 24" fill="none" stroke="#fff" stroke-width="1.5"><path d="M4 19h16M6 16v-4M11 16V9M16 16V6"/></svg></span><span class="benefit-text">More leads grow the companies revenue</span></li>
    <li class="benefit"><span class="benefit-icon"><svg width="24" height="24" viewBox="0 0 24 24" fill="none" stroke="#fff" stroke-width="1.5"><circle cx="12" cy="12" r="8"/><path d="M12 7v5l3 2"/></svg></span><span class="benefit-text">Less time managing other advertising models</span></li>
  </ul>

  <div class="abs services-line" style="top:680px;height:62px"></div>
  <div class="abs services-label">OUR 3 SERVICES</div>
  <div class="abs services-line" style="top:952px;height:78px"></div>

  <div class="abs price" style="left:461px;top:688px"><span class="price-amount"><sup>$</sup>250</span><span class="price-each">EACH</span></div>
  <div class="abs price" style="left:461px;top:828px"><span class="price-amount"><sup>$</sup>275</span><span class="price-each">EACH</span></div>
  <div class="abs price" style="left:461px;top:970px"><span class="price-amount"><sup>$</sup>375</span><span class="price-each">EACH</span></div>

  <ul class="abs plan" style="top:688px">
    <li><svg width="13" height="13" viewBox="0 0 14 14"><circle cx="7" cy="7" r="7" fill="#a45f28"/><path d="M4 7.2l2 2 4-4.2" fill="none" stroke="#fff" stroke-width="1.6"/></svg>We send you the lead</li>
    <li><svg width="13" height="13" viewBox="0 0 14 14"><circle cx="7" cy="7" r="7" fill="#a45f28"/><path d="M4 7.2l2 2 4-4.2" fill="none" stroke="#fff" stroke-width="1.6"/></svg>You and your team set the appointment</li>
    <li><svg width="13" height="13" viewBox="0 0 14 14"><circle cx="7" cy="7" r="7" fill="#a45f28"/><path d="M4 7.2l2 2 4-4.2" fill="none" stroke="#fff" stroke-width="1.6"/></svg>Setting the appointment is up to you</li>
  </ul>
  <div class="abs divider" style="top:806px"></div>
  <ul class="abs plan" style="top:825px">
    <li><svg width="13" height="13" viewBox="0 0 14 14"><circle cx="7" cy="7" r="7" fill="#a45f28"/><path d="M4 7.2l2 2 4-4.2" fill="none" stroke="#fff" stroke-width="1.6"/></svg>We send you the lead</li>
    <li><svg width="13" height="13" viewBox="0 0 14 14"><circle cx="7" cy="7" r="7" fill="#a45f28"/><path d="M4 7.2l2 2 4-4.2" fill="none" stroke="#fff" stroke-width="1.6"/></svg>You and your team set the appointment</li>
    <li><svg width="13" height="13" viewBox="0 0 14 14"><circle cx="7" cy="7" r="7" fill="#a45f28"/><path d="M4 7.2l2 2 4-4.2" fill="none" stroke="#fff" stroke-width="1.6"/></svg>We guarantee the appointment</li>
    <li><svg width="13" height="13" viewBox="0 0 14 14"><circle cx="7" cy="7" r="7" fill="#a45f28"/><path d="M4 7.2l2 2 4-4.2" fill="none" stroke="#fff" stroke-width="1.6"/></svg>Return unset appointments for a replacement</li>
  </ul>
  <div class="abs divider" style="top:980px"></div>
  <ul class="abs plan" style="top:1003px">
    <li><svg width="13" height="13" viewBox="0 0 14 14"><circle cx="7" cy="7" r="7" fill="#a45f28"/><path d="M4 7.2l2 2 4-4.2" fill="none" stroke="#fff" stroke-width="1.6"/></svg>We are your call center</li>
    <li><svg width="13" height="13" viewBox="0 0 14 14"><circle cx="7" cy="7" r="7" fill="#a45f28"/><path d="M4 7.2l2 2 4-4.2" fill="none" stroke="#fff" stroke-width="1.6"/></svg>We generate the lead</li>
    <li><svg width="13" height="13" viewBox="0 0 14 14"><circle cx="7" cy="7" r="7" fill="#a45f28"/><path d="M4 7.2l2 2 4-4.2" fill="none" stroke="#fff" stroke-width="1.6"/></svg>We set the appointment</li>
  </ul>

  <div class="abs brand-footer">The Shelf Sage</div>

  <div class="abs contact">
    <span><svg width="16" height="16" viewBox="0 0 16 16"><circle cx="8" cy="8" r="8" fill="#a45f28"/><path d="M5.2 4.5l1.5-.3.8 1.8-1 .8a5 5 0 002.3 2.3l.8-1 1.8.8-.3 1.5c-3.2.2-6.1-2.7-5.9-5.9z" fill="#fff"/></svg>704-555-0183</span>
    <span><svg width="16" height="16" viewBox="0 0 16 16"><circle cx="8" cy="8" r="8" fill="#a45f28"/><rect x="4" y="5.2" width="8" height="5.6" fill="#fff"/><path d="M4 5.4l4 3 4-3" fill="none" stroke="#a45f28" stroke-width=".9"/></svg>leads@TheShelfSage.example</span>
  </div>
  <div class="abs web-bar">
    <svg width="15" height="15" viewBox="0 0 16 16" fill="none" stroke="#fff" stroke-width="1.2"><circle cx="8" cy="8" r="6.5"/><ellipse cx="8" cy="8" rx="3" ry="6.5"/><path d="M1.5 8h13"/></svg>
    <span>www.<b>shelfsagegreenville</b>.example</span>
  </div>
</main>
</body>
</html>
```